Business card revamp

we are refrigeration mechanic i need a modern professional double side business card using my current branding
The card information must have site address~ 17 Whitlow st cobram, Vic 3644 postal address~ P.o. Box 862 cobram,Vic 3643 Phone Number~0358149637 Fax Nunber~0358260518 Email address~ brucet@pelvanor.com.au Title~ Manager Licence numbers~ AU47391, NSW 681329K Web site~ www.frostrimvane.com.au

Industry/Entity Type

Business

```html
<!DOCTYPE html>
<html lang="en">
<head>
<meta charset="utf-8">
<title>Refrigeration Mechanic – Business Card</title>
<link href="https://fonts.googleapis.com/css2?family=Cabin:wght@700&family=Montserrat:wght@800&display=swap" rel="stylesheet">
<style>
  :root{
    --brand-red:#c4120f;
    --back-red-centre:#b3170f;
    --back-red-edge:#8f2c24;
    --ink:#111111;
    --paper:#ffffff;
    --frame:#555555;
    --badge-orange:#e8742a;
    --badge-cream:#f6d9a8;
    --figure-blue:#5a86c0;
    --figure-skin:#e7b996;
  }
  *{margin:0;padding:0;box-sizing:border-box}
  html,body{width:914px;height:1200px;overflow:hidden;background:var(--paper)}
  .canvas{position:relative;width:914px;height:1200px;background:var(--paper)}

  .card{position:absolute;left:12px;width:888px;height:512px;overflow:hidden}

  /* Front */
  .card--front{top:54px;background:var(--paper);border:1.5px solid var(--frame)}
  .side-band{position:absolute;left:0;top:0;width:173px;height:100%;background:var(--brand-red)}
  .badge-art{position:absolute;left:38px;top:14px;width:104px;height:102px;border-radius:6px;
    background:linear-gradient(180deg,var(--badge-orange) 0%,var(--badge-cream) 55%,var(--figure-blue) 100%)}
  .band-title{position:absolute;left:16px;bottom:34px;writing-mode:vertical-rl;transform:rotate(180deg);
    font-family:'Montserrat',sans-serif;font-weight:800;font-size:29px;line-height:34px;color:var(--paper);letter-spacing:.5px}
  .mechanic-art{position:absolute;left:184px;top:196px;width:104px;height:310px;border-radius:40px 40px 10px 10px;
    background:linear-gradient(180deg,var(--figure-skin) 0%,var(--figure-blue) 35%,#3f5f96 100%)}

  .contact-list{position:absolute;left:303px;top:98px;list-style:none;
    font-family:'Cabin',sans-serif;font-weight:700;font-size:19px;line-height:27px;color:var(--ink)}
  .contact-list li{display:flex}
  .contact-label{width:267px}
  .contact-label::before{content:"-";display:inline-block;width:19px}
  .website{position:absolute;right:18px;top:444px;font-family:'Cabin',sans-serif;font-weight:700;font-size:23px;color:var(--ink)}

  /* Back */
  .card--back{top:672px;height:511px;border:1.5px solid #333;
    background:radial-gradient(ellipse 60% 65% at 50% 50%,var(--back-red-centre) 0%,var(--back-red-edge) 100%)}
  .badge-art--large{left:306px;top:52px;width:258px;height:244px;border-radius:10px}
  .back-title{position:absolute;left:0;right:0;top:302px;text-align:center;
    font-family:'Montserrat',sans-serif;font-weight:800;font-size:46px;color:var(--paper);letter-spacing:.5px}
</style>
</head>
<body>
<main class="canvas">
  <section class="card card--front">
    <div class="side-band">
      <div class="badge-art" role="img" aria-label="Badge illustration of a refrigeration mechanic holding gauges"></div>
      <p class="band-title">REFRIGERATION<br>MECHANIC</p>
    </div>
    <div class="mechanic-art" role="img" aria-label="Cartoon mechanic in cap and uniform holding a toolbox, giving thumbs up"></div>
    <ul class="contact-list">
      <li><span class="contact-label">Site Address</span><span>: 17 Whitlow st cobram, Vic 3644</span></li>
      <li><span class="contact-label">Postal Address</span><span>: P.o. Box 862 cobram,Vic 3643</span></li>
      <li><span class="contact-label">Phone Number</span><span>: 0358149637</span></li>
      <li><span class="contact-label">Fax Nunber</span><span>: 0358260518</span></li>
      <li><span class="contact-label">Email Address</span><span>: brucet@pelvanor.com.au</span></li>
      <li><span class="contact-label">Title</span><span>: Manager</span></li>
      <li><span class="contact-label">Licence Numbers</span><span>: AU47391, NSW 681329K</span></li>
    </ul>
    <p class="website">Web site : www.frostrimvane.com.au</p>
  </section>

  <section class="card card--back">
    <div class="badge-art badge-art--large" role="img" aria-label="Badge illustration of a refrigeration mechanic holding pressure gauges"></div>
    <h1 class="back-title">REFRIGERATION MECHANIC</h1>
  </section>
</main>
</body>
</html>
```